Harvest Gathering event flyer

I would like a church event flyer designed. The event is called "HARVEST GATHERING 2018". I am looking for a professional, yet catchy design that uses our brand colors and logo creatively while communicating key information of the event effectively.

1. The logo is attached in two color formats. The designer has the choice to use them as he/she want.

2. The location of the event is: Lindqvist Community Center, 482 Tamsworth Street, Portland, ME 04102
3. Time and date of event. The designer can organize and format the date and time as he/she pleases.
December 28th, 29th @ 7:00PM
December 30th @ 10:00AM
4. The topic of the event is "Tongues of fire". The designer is free to use this phrase as he/she pleases to create a good composition.
5. Speaker: Prophet Marcus Obuya
6. Contact information: contact@cedarbrookfellowship.org - Telephone number: 207 555 0148

7. I would also like the following three words on the flyer. These words describe the focus of the event: FIRE, REVIVAL, PROPHETIC

```html
<!DOCTYPE html>
<html lang="en">
<head>
<meta charset="utf-8">
<title>Harvest Gathering 2018 – Flyer</title>
<link href="https://fonts.googleapis.com/css2?family=Poiret+One&family=Oswald:wght@500&family=Quicksand:wght@400;500&display=swap" rel="stylesheet">
<style>
  :root {
    --stage: #3a3a38;
    --paper: #0b0906;
    --photo-warm: #3b2f18;
    --photo-glass: #4a4c5a;
    --ink: #f4f1ea;
    --ink-soft: #d9d3c6;
    --rule: #cfc9bd;
    --topic: #e7a774;
    --speaker: #7f93d6;
    --brand: #e4572e;
  }
  html, body {
    margin: 0;
    width: 1200px;
    height: 810px;
    overflow: hidden;
    background: var(--stage);
  }
  .flyer {
    position: absolute;
    left: 310px;
    top: 28px;
    width: 580px;
    height: 754px;
    background: var(--paper);
    overflow: hidden;
    color: var(--ink);
    font-family: "Quicksand", sans-serif;
  }
  .flyer__backdrop {
    position: absolute;
    inset: 0;
    background:
      radial-gradient(ellipse 22% 30% at 52% 36%, var(--photo-glass) 0%, rgba(74,76,90,0.35) 60%, transparent 100%),
      radial-gradient(ellipse 70% 55% at 75% 55%, var(--photo-warm) 0%, rgba(59,47,24,0.4) 55%, transparent 100%),
      linear-gradient(180deg, #050403 0%, #1a150c 45%, #120e07 75%, #060504 100%);
  }
  .brand {
    position: absolute;
    left: 30px;
    top: 32px;
    display: flex;
    align-items: center;
    gap: 7px;
  }
  .brand__dot {
    width: 9px;
    height: 9px;
    border-radius: 50%;
    background: var(--brand);
  }
  .brand__name {
    font-family: "Quicksand", sans-serif;
    font-weight: 500;
    font-size: 17px;
    letter-spacing: 2px;
    color: var(--ink);
  }
  .content {
    position: absolute;
    left: 0;
    right: 0;
    top: 115px;
    text-align: center;
  }
  .title {
    margin: 0;
    font-family: "Poiret One", sans-serif;
    font-weight: 400;
    font-size: 46px;
    line-height: 1.02;
    letter-spacing: 3px;
  }
  .rule {
    height: 1px;
    background: var(--rule);
    margin: 16px auto;
  }
  .rule--wide { width: 400px; }
  .rule--short { width: 260px; margin: 12px auto; }
  .focus {
    font-family: "Oswald", sans-serif;
    font-weight: 500;
    font-size: 48px;
    line-height: 1;
    letter-spacing: 0;
    transform: scaleY(1.25);
    margin: 20px 0 18px;
  }
  .topic, .speaker {
    margin: 8px 0 0;
    font-size: 18px;
    letter-spacing: 1.5px;
    text-transform: uppercase;
  }
  .topic__label { color: var(--topic); }
  .speaker__label { color: var(--speaker); }
  .dates {
    margin: 10px 0 0;
    font-size: 21px;
    line-height: 1.3;
  }
  .venue {
    margin: 14px 0 0;
    font-size: 14px;
    line-height: 1.45;
    letter-spacing: 1px;
    color: var(--ink-soft);
  }
  .contact {
    position: absolute;
    left: 0;
    right: 0;
    bottom: 34px;
    text-align: center;
    font-size: 10.5px;
    letter-spacing: 1.6px;
    text-transform: uppercase;
  }
  .contact__phone { margin-left: 12px; }
</style>
</head>
<body>
  <article class="flyer">
    <div class="flyer__backdrop" role="img" aria-label="Dim church interior with a stained glass window above the altar"></div>

    <div class="brand">
      <span class="brand__dot"></span>
      <span class="brand__name">KESTREL</span>
    </div>

    <section class="content">
      <h1 class="title">HARVEST<br>GATHERING<br>2018</h1>
      <div class="rule rule--wide"></div>
      <p class="focus">FIRE · REVIVAL · PROPHETIC</p>
      <p class="topic"><span class="topic__label">Topic - </span>Tongues of Fire</p>
      <div class="rule rule--short"></div>
      <p class="speaker"><span class="speaker__label">Speaker - </span>Prophet Marcus Obuya</p>
      <p class="dates">December 28th, 29th @ 7pm<br>December 30th @ 10 am</p>
      <p class="venue">Lindqvist Community Center<br>482 Tamsworth Street, Portland, ME 04102</p>
    </section>

    <footer class="contact">
      For more info contact - contact@cedarbrookfellowship.org<span class="contact__phone">207 555 0148</span>
    </footer>
  </article>
</body>
</html>
```